Business Card Design for Portrait photography professional

We are a small company specializing in portrait photography (weddings, family, couples, children, newborn, pregnant, etc.) Occasionally we do business portraits too and do some other type of photography. We need a business card which would fit into the same look and feel as our website theme (lumvika.com - under construction currently).
Our target customer base lies within mid- to upmarket. We want our business cards to convey a feeling of quality, solidness and a bit luxury.
Design should be universal and usable on 85mmx55mm, 90mmx50mm and 90mmx55mm
one extra file (PSD of a website didn't fit into the allowed updoad, therefore has put it into my filecrate: https://www.filecrate-example.net/s/qt7wk2rbvx9dmhe/website%20theme%20PSD.psd)

Target Market(s)

mostly private people, 25-60 years old, mostly well established.

Industry/Entity Type

Portrait Photography

Requirements
Must have
• 2 sided design (print on both sides of the business card).
Must include:
business name, logo, URL (lumvika.no) , employee name, email address, and phone number.
Colorscheme of the website lumvika.no / lumvika.com

```html
<!DOCTYPE html>
<html lang="en">
<head>
<meta charset="utf-8">
<title>Lumvika — Business Card</title>
<link rel="stylesheet" href="https://fonts.googleapis.com/css2?family=Comfortaa:wght@600;700&family=Questrial&display=swap">
<style>
  :root {
    --page-bg: #d9d9d9;
    --card-dark: #2a2725;
    --card-mid: #3b3735;
    --card-glow: #4d4946;
    --text-light: #f2f0ec;
    --text-muted: #c9c5c0;
    --mark-grey: #8a8683;
    --ring-outer: #1c1a19;
    --ring-inner: #6a6663;
    --icon-bg: #77726e;
  }
  * { margin: 0; padding: 0; box-sizing: border-box; }
  html, body {
    width: 1200px; height: 900px; overflow: hidden;
    background: var(--page-bg);
  }
  .stage {
    position: relative; width: 1200px; height: 900px;
    display: flex; align-items: center; justify-content: center; gap: 40px;
  }
  .card {
    position: relative; width: 500px; height: 310px;
    border: 3px solid #f4f4f4;
    box-shadow: 0 6px 18px rgba(0,0,0,0.25);
    overflow: hidden;
  }
  /* Front side */
  .card--front {
    background: radial-gradient(ellipse at 50% 45%, var(--card-mid) 0%, var(--card-dark) 75%);
  }
  .viewfinder-marks { position: absolute; inset: 0; }
  .brand-lens {
    position: absolute; left: 50%; top: 46%;
    transform: translate(-50%, -50%);
    display: flex; flex-direction: column; align-items: center; gap: 14px;
  }
  .brand-lens__disc {
    width: 150px; height: 150px; border-radius: 50%;
    background: radial-gradient(circle at 50% 45%, var(--ring-inner) 0%, #3e3a38 55%, var(--ring-outer) 100%);
    box-shadow: 0 4px 14px rgba(0,0,0,0.55);
  }
  .brand-lens__name {
    font-family: "Questrial", sans-serif;
    font-size: 20px; color: var(--text-light); letter-spacing: 1px;
  }
  /* Back side */
  .card--back {
    background: radial-gradient(ellipse at 58% 48%, var(--card-glow) 0%, var(--card-mid) 35%, var(--card-dark) 85%);
  }
  .identity {
    position: absolute; left: 32px; top: 52px;
    display: flex; align-items: center; gap: 20px;
  }
  .identity__badge {
    width: 58px; height: 58px; border-radius: 50%;
    background: radial-gradient(circle, #5a5653 0%, #2f2c2a 70%);
    border: 3px solid #6b6764;
  }
  .identity__person {
    font-family: "Comfortaa", sans-serif; font-weight: 700;
    font-size: 13px; color: var(--text-light);
  }
  .identity__title {
    font-family: "Comfortaa", sans-serif; font-weight: 700;
    font-size: 22px; color: var(--text-light); margin-top: 2px;
  }
  .contacts {
    position: absolute; left: 40px; top: 200px;
    list-style: none;
    font-family: "Questrial", sans-serif; font-size: 13px; color: var(--text-muted);
  }
  .contacts li { display: flex; align-items: center; gap: 8px; height: 20px; }
  .contacts svg { width: 10px; height: 10px; }
</style>
</head>
<body>
<main class="stage">
  <section class="card card--front" aria-label="Card front">
    <svg class="viewfinder-marks" width="500" height="310" viewBox="0 0 500 310" aria-hidden="true">
      <g fill="none" stroke="var(--mark-grey)" stroke-width="2">
        <path d="M40 62 V40 H62"/>
        <path d="M438 40 H460 V62"/>
        <path d="M40 248 V270 H62"/>
        <path d="M438 270 H460 V248"/>
      </g>
    </svg>
    <div class="brand-lens">
      <div class="brand-lens__disc"></div>
      <span class="brand-lens__name">lumvika.no</span>
    </div>
  </section>

  <section class="card card--back" aria-label="Card back">
    <div class="identity">
      <div class="identity__badge"></div>
      <div>
        <p class="identity__person">K.L. Marsden</p>
        <p class="identity__title">Personal Photographer</p>
      </div>
    </div>
    <ul class="contacts">
      <li>
        <svg viewBox="0 0 10 10" aria-hidden="true"><rect width="10" height="10" fill="var(--icon-bg)"/><circle cx="5" cy="5" r="2.2" fill="none" stroke="#2a2725" stroke-width="1"/></svg>
        <span>: info@lumvika.no</span>
      </li>
      <li>
        <svg viewBox="0 0 10 10" aria-hidden="true"><rect x="2.5" y="0.5" width="5" height="9" rx="1" fill="var(--icon-bg)"/><rect x="3.5" y="1.8" width="3" height="3" fill="#2a2725"/></svg>
        <span>: (+47) 412-30-658</span>
      </li>
      <li>
        <svg viewBox="0 0 10 10" aria-hidden="true"><rect width="10" height="10" fill="var(--icon-bg)"/><path d="M2 3 L3.5 7 L5 4.5 L6.5 7 L8 3" fill="none" stroke="#2a2725" stroke-width="1"/></svg>
        <span>: www.lumvika.no</span>
      </li>
    </ul>
  </section>
</main>
</body>
</html>
```